Simple, elegant, business card design required

Hi designers,I am looking for a simple yet elegant business card design.

Please make use of my logo (attached); you are free to tweak the logo should you wish to do so.

Our business is involved in many different fields - almost all of them involved in some form of "design", so that's really one of the key things I want to portray. I do not wish to specify which field of design, exactly.

I prefer white on black (or just monochromatic), but if you have a different, creative idea, I am open to that too.

You can use artsy photographs provided that you have the license to use those. Please feel free to ask me any questions.

Target Market(s)

High-end customers looking for design consultancy

Industry/Entity Type

Business

Contact Information for Business Card

Name: Gareth Pellwinter
Position: Creative Director
Mobile: +150963218745
Address: Morrow Lane, Halvercombe upon Tarn, Brackenshire HT14 2JT
Website: corvastudio.com (not launched yet)

Requirements
Must have
• Design layout must be clean, original, and text must be readable when printed.
Should not have
• ~ No business card templates please. Anyone using this will be reported.
• ~ Please don't spam entries.

```html
<!DOCTYPE html>
<html lang="en">
<head>
<meta charset="utf-8">
<title>Corvastudio – Business Card</title>
<link rel="stylesheet" href="https://fonts.googleapis.com/css2?family=Alegreya+Sans:wght@400;500&display=swap">
<style>
  :root {
    --backdrop: #e6e7e9;
    --card: #ffffff;
    --ink: #111111;
    --band: #000000;
    --band-text: #ffffff;
  }
  * { box-sizing: border-box; margin: 0; padding: 0; }
  html, body {
    width: 1200px;
    height: 1200px;
    overflow: hidden;
    background: var(--backdrop);
    font-family: "Alegreya Sans", "Helvetica Neue", Arial, sans-serif;
    font-variant-numeric: lining-nums;
    color: var(--ink);
  }
  .business-card {
    position: absolute;
    left: 100px;
    top: 314px;
    width: 1000px;
    height: 572px;
    background: var(--card);
  }
  .identity-band {
    position: absolute;
    left: 0;
    top: 109px;
    width: 625px;
    height: 163px;
    background: var(--band);
    color: var(--band-text);
  }
  .identity-band .person-name {
    position: absolute;
    left: 53px;
    top: 44px;
    font-size: 34px;
    font-weight: 400;
    line-height: 1;
  }
  .identity-band .person-role {
    position: absolute;
    left: 53px;
    top: 88px;
    font-size: 27px;
    font-weight: 400;
    line-height: 1;
  }
  .identity-band .brand-dot {
    position: absolute;
    left: 552px;
    top: 57px;
    width: 48px;
    height: 48px;
  }
  .brand-name {
    position: absolute;
    left: 652px;
    top: 172px;
    font-size: 36px;
    font-weight: 500;
    letter-spacing: 5px;
    line-height: 1;
    text-transform: uppercase;
  }
  .contact-details {
    position: absolute;
    left: 53px;
    top: 346px;
    font-size: 27px;
    line-height: 32px;
  }
  .contact-details .address {
    margin-top: 18px;
    line-height: 38px;
  }
</style>
</head>
<body>
  <article class="business-card">
    <div class="identity-band">
      <div class="person-name">Gareth Pellwinter</div>
      <div class="person-role">Creative Director</div>
      <svg class="brand-dot" viewBox="0 0 48 48" aria-hidden="true">
        <circle cx="24" cy="24" r="21" fill="none" stroke="#ffffff" stroke-width="4"/>
      </svg>
    </div>
    <div class="brand-name">Corvastudio</div>
    <div class="contact-details">
      <div class="phone">+1 5096 3218 745</div>
      <div class="website">www.corvastudio.com</div>
      <div class="address">Morrow Lane, Halvercombe upon Tarn,<br>Brackenshire HT14 2JT</div>
    </div>
  </article>
</body>
</html>
```